Bref créative
Business Card Design for Law Firm
Harlow Legal Partners
Professional
Derek M. Falbo
Trial Lawyer
2730 Birchwood Avenue
North Annex - Suite 2100
Philadelphia, PA 19102
555-014-2737 (use as place holder)
derek@harlowcounsel.example
www.harlowcounsel.example
I am looking for a bold logo and business card design for a start-up law firm based in Philadelphia and with offices in PA and NJ. Harlow Legal Partners is led by trial attorneys and specializes in catastrophic personal injury litigation stemming from construction / industrial accidents, truck/auto accidents, defective products, falls, and medical malpractice.
New #s for phone and fax will be supplied upon selection of winning design.
Areas of Expertise:
- Personal Injury
- Wrongful Death
- Construction Accidents
- Work Injuries
- Car & Truck Accidents
- Motorcycle Accidents
- Medical Malpractice
- Nursing Home Abuse
- Premises Liability
- Longshore / Maritime
- Commercial Litigation
White Version
Black Version

```html
<!DOCTYPE html>
<html lang="en">
<head>
<meta charset="utf-8">
<title>Harlow Legal Partners – Stationery Set</title>
<link href="https://fonts.googleapis.com/css2?family=Cinzel:wght@600&family=Open+Sans:wght@400;600&display=swap" rel="stylesheet">
<style>
  :root{
    --bg:#8e8e8e;
    --bg-dark:#7f7f7f;
    --blue:#1f74d6;
    --blue-deep:#0b4ea8;
    --blue-soft:#d9e8f8;
    --silver:#b9bec6;
    --paper:#ffffff;
    --ink:#5a5f66;
    --shadow:rgba(0,0,0,.28);
  }
  *{box-sizing:border-box;margin:0;padding:0}
  html,body{width:1200px;height:480px;overflow:hidden}
  body{background:var(--bg);font-family:"Open Sans",sans-serif;color:var(--ink);position:relative}
  .piece{position:absolute;background:var(--paper);box-shadow:0 2px 6px var(--shadow);overflow:hidden}
  .piece svg.band{position:absolute;left:0;top:0;width:100%;height:100%}
  .brand{font-family:"Cinzel",serif;font-weight:600;color:var(--blue);letter-spacing:.06em;line-height:1.1;position:absolute;text-transform:uppercase}
  .brand.on-blue{color:var(--paper)}
  .contact{position:absolute;font-size:5px;line-height:1.45;color:var(--ink);white-space:nowrap}
  .contact.on-blue{color:var(--paper)}
  .contact strong{font-weight:600;color:var(--blue-deep)}

  /* small cards, left */
  .card-front-left{left:24px;top:163px;width:86px;height:50px}
  .card-back-left{left:24px;top:240px;width:86px;height:50px}
  /* letterhead */
  .letterhead{left:161px;top:79px;width:252px;height:377px}
  .letterhead .watermark{position:absolute;left:76px;top:170px;width:100px;height:100px;border-radius:50%;border:10px solid var(--blue-soft);opacity:.7}
  /* cards, middle */
  .card-horizontal{left:444px;top:84px;width:175px;height:72px}
  .card-vertical{left:636px;top:91px;width:60px;height:113px}
  /* envelope */
  .envelope-front{left:444px;top:228px;width:288px;height:132px}
  .envelope-back{left:444px;top:365px;width:288px;height:96px}
  /* folder */
  .folder{left:768px;top:79px;width:413px;height:377px;background:transparent;box-shadow:none;overflow:visible}
  .folder-left{position:absolute;left:0;top:0;width:206px;height:377px;background:var(--paper);box-shadow:0 2px 6px var(--shadow);overflow:hidden}
  .folder-right{position:absolute;left:206px;top:0;width:207px;height:377px;background:var(--paper);box-shadow:0 2px 6px var(--shadow)}
  .folder-left .watermark{position:absolute;left:48px;top:110px;width:90px;height:90px;border-radius:50%;border:12px solid rgba(255,255,255,.28)}
  .folder-pocket{position:absolute;left:0;bottom:0;width:100%;height:100%}
  .folder-mark{position:absolute;left:262px;top:138px;display:flex;align-items:center;gap:8px}
  .folder-mark .divider{width:1px;height:34px;background:var(--blue)}
  .folder-mark .brand{position:static;font-size:15px}
</style>
</head>
<body>

<!-- business card, front -->
<div class="piece card-front-left">
  <svg class="band" viewBox="0 0 86 50" preserveAspectRatio="none">
    <path d="M0,0 H86 V50 H52 Q40,24 0,18 Z" fill="var(--blue)"/>
    <path d="M0,21 Q40,27 50,50" stroke="var(--silver)" stroke-width="1.2" fill="none"/>
  </svg>
  <div class="brand" style="left:6px;top:28px;font-size:5.5px">Harlow Legal<br>Partners</div>
</div>

<!-- business card, back -->
<div class="piece card-back-left">
  <svg class="band" viewBox="0 0 86 50" preserveAspectRatio="none">
    <path d="M0,0 H86 V8 Q40,10 0,20 Z" fill="var(--blue)"/>
    <path d="M0,23 Q40,13 86,11" stroke="var(--silver)" stroke-width="1" fill="none"/>
  </svg>
  <div class="brand" style="left:6px;top:24px;font-size:4px">Harlow Legal<br>Partners</div>
  <div class="contact" style="left:44px;top:22px;font-size:3.4px"><strong>Derek M. Falbo</strong><br>2730 Birchwood Avenue<br>North Annex - Suite 2100<br>555-014-2737</div>
</div>

<!-- letterhead -->
<div class="piece letterhead">
  <svg class="band" viewBox="0 0 252 377" preserveAspectRatio="none">
    <path d="M0,0 H252 V30 Q130,40 0,100 Z" fill="var(--blue)"/>
    <path d="M0,106 Q130,44 252,36" stroke="var(--silver)" stroke-width="2.5" fill="none"/>
  </svg>
  <div class="brand on-blue" style="left:10px;top:10px;font-size:7px">Harlow Legal Partners</div>
  <div class="watermark" aria-hidden="true"></div>
  <div class="contact" style="left:10px;top:356px;font-size:4px">2730 Birchwood Avenue · North Annex - Suite 2100 · 555-014-2737 · www.harlowcounsel.example</div>
</div>

<!-- business card, horizontal -->
<div class="piece card-horizontal">
  <svg class="band" viewBox="0 0 175 72" preserveAspectRatio="none">
    <path d="M0,0 H175 V14 Q90,18 0,42 Z" fill="var(--blue)"/>
    <path d="M0,45 Q90,20 175,17" stroke="var(--silver)" stroke-width="1.5" fill="none"/>
  </svg>
  <div class="contact on-blue" style="left:120px;top:4px;font-size:4px"><strong style="color:#fff">Derek M. Falbo</strong><br>Trial Lawyer</div>
  <div class="brand" style="left:8px;top:50px;font-size:5.5px">Harlow Legal<br>Partners</div>
  <div class="contact" style="left:80px;top:40px;font-size:4px">2730 Birchwood Avenue<br>North Annex - Suite 2100<br>555-014-2737<br>derek@harlowcounsel.example</div>
</div>

<!-- business card, vertical -->
<div class="piece card-vertical">
  <svg class="band" viewBox="0 0 60 113" preserveAspectRatio="none">
    <path d="M0,0 H60 V20 Q30,22 0,38 Z" fill="var(--blue)"/>
    <path d="M0,41 Q30,25 60,23" stroke="var(--silver)" stroke-width="1.2" fill="none"/>
  </svg>
  <div class="brand" style="left:5px;top:48px;font-size:4.5px">Harlow Legal<br>Partners</div>
  <div class="contact" style="left:5px;top:70px;font-size:3.4px"><strong>Derek M. Falbo</strong><br>555-014-2737<br>www.harlowcounsel.example<br>Skype: dfalbo52</div>
</div>

<!-- envelope, front -->
<div class="piece envelope-front">
  <svg class="band" viewBox="0 0 288 132" preserveAspectRatio="none">
    <path d="M0,0 H288 V18 Q150,22 0,58 Z" fill="var(--blue)"/>
    <path d="M0,62 Q150,25 288,22" stroke="var(--silver)" stroke-width="2" fill="none"/>
  </svg>
  <div class="brand on-blue" style="left:10px;top:10px;font-size:6.5px">Harlow Legal Partners</div>
  <div class="contact" style="left:12px;top:64px;font-size:4.5px">2730 Birchwood Avenue<br>North Annex - Suite 2100<br>Philadelphia, PA 19102</div>
</div>

<!-- envelope, back -->
<div class="piece envelope-back">
  <svg class="band" viewBox="0 0 288 96" preserveAspectRatio="none">
    <path d="M0,0 H288 V96 H0 Z" fill="var(--blue)"/>
    <path d="M0,0 H288 L164,62 Q144,72 124,62 Z" fill="var(--paper)" stroke="var(--silver)" stroke-width="1.5"/>
  </svg>
  <div class="brand" style="left:0;width:288px;text-align:center;top:44px;font-size:4.5px">Harlow Legal Partners</div>
</div>

<!-- presentation folder -->
<div class="piece folder">
  <div class="folder-left">
    <svg class="band" viewBox="0 0 206 377" preserveAspectRatio="none">
      <defs>
        <linearGradient id="folderBlue" x1="0" y1="0" x2="1" y2="1">
          <stop offset="0" stop-color="var(--blue)"/>
          <stop offset="1" stop-color="var(--blue-deep)"/>
        </linearGradient>
      </defs>
      <path d="M0,0 H206 V377 H0 Z" fill="url(#folderBlue)"/>
      <path d="M0,290 Q110,270 206,300 V377 H0 Z" fill="var(--paper)"/>
      <path d="M0,286 Q110,266 206,296" stroke="var(--silver)" stroke-width="2" fill="none"/>
    </svg>
    <div class="watermark" aria-hidden="true"></div>
  </div>
  <div class="folder-right">
    <svg class="folder-pocket" viewBox="0 0 207 377" preserveAspectRatio="none">
      <path d="M0,300 Q100,285 207,300" stroke="var(--silver)" stroke-width="1.5" fill="none"/>
      <path d="M150,340 L170,326 L190,340" stroke="var(--silver)" stroke-width="1" fill="none"/>
    </svg>
  </div>
  <div class="folder-mark">
    <span class="divider"></span>
    <span class="brand">Harlow<br>Legal Partners</span>
  </div>
  <div class="contact" style="left:262px;top:328px;font-size:4px">2730 Birchwood Avenue · 555-014-2737<br>www.harlowcounsel.example</div>
</div>

</body>
</html>
```